Fire Hydrant Repair Parts Flyer

We need a flyer advertising both fire hydrant parts and the manufacturers that we are stocking. Our company is Coastal Flowline Supply and we are a parts distributor who sells directly to contractors. I have attached an example flyer that advertises some other parts we stock. We don't want it to look exactly like the old flyer, but we would like it to be structured similarly. I have also attached a background image for the flyer as well as some pictures of the parts we are stocking. I have also attached pictures of the manufacturer logos that we are stocking. We are trying to convey the parts that we are stocking which are: "Traffic Repair Kits", "Main Valve Repair Kits", "Extension Kits", "Replacement Caps & Gaskets", "Replacement Nozzles", Adjustable Hydrant Wrenches", "Hydrant Diffusers", & "Hydrant Oil". I have attached pictures of some of these items that we would like placed on the flyer. Let me know if you have any questions at all.

```html
<!DOCTYPE html>
<html lang="en">
<head>
<meta charset="utf-8">
<title>Coastal Flowline Supply – Fire Hydrant Parts</title>
<link href="https://fonts.googleapis.com/css2?family=Roboto+Condensed:wght@400;700&display=swap" rel="stylesheet">
<style>
  :root{
    --blue:#2f3f9f;
    --panel-blue:#3c52a5;
    --red:#e81d4f;
    --red-deep:#c8173f;
    --ink:#454545;
    --band:#e5e6e8;
    --white:#ffffff;
  }
  *{margin:0;padding:0;box-sizing:border-box}
  html,body{width:848px;height:1200px;overflow:hidden;background:var(--white)}
  body{font-family:"Roboto Condensed",Arial,sans-serif}
  .flyer{position:relative;width:848px;height:1200px;overflow:hidden;background:var(--white)}
  .hero-photo{position:absolute;left:0;top:0;width:848px;height:660px;
    background:
      radial-gradient(ellipse 180px 300px at 150px 330px,#c8202c 0%,#b81d28 55%,rgba(184,29,40,0) 100%),
      linear-gradient(100deg,#6e9a4a 0%,#7fa75a 22%,#9aa3a8 40%,#d9dde0 62%,#f4f5f6 80%,#ffffff 100%);}
  .shapes{position:absolute;left:0;top:0}
  .brand{position:absolute;left:470px;top:18px;display:flex;align-items:center;gap:12px;color:var(--blue)}
  .brand-mark{width:34px;height:34px;border-radius:50%;background:var(--blue)}
  .brand-name{font-weight:400;font-size:30px;line-height:1;letter-spacing:.2px}
  .headline{position:absolute;right:30px;top:212px;text-align:right;font-weight:700;line-height:.82}
  .headline .main{display:block;color:var(--blue);font-size:66px;letter-spacing:.5px}
  .headline .sub{display:block;color:var(--red);font-size:37px;margin-top:14px;letter-spacing:.5px}
  .contact{position:absolute;right:33px;top:436px;text-align:right;color:var(--white)}
  .contact .cta{font-weight:700;font-size:30px;line-height:1.1}
  .contact .phone{display:flex;align-items:center;justify-content:flex-end;gap:8px;font-weight:700;font-size:52px;line-height:1;margin-top:2px}
  .contact .web{font-size:27px;line-height:1.2;margin-top:2px}
  .parts-list{position:absolute;left:34px;top:690px;width:322px;list-style:none}
  .parts-list li{display:flex;align-items:center;gap:11px;height:48.3px;border-bottom:1px dashed #8a8a8a;
    font-weight:700;font-size:27px;color:var(--ink);white-space:nowrap}
  .parts-list li:last-child{border-bottom:none}
  .parts-list svg{flex:none}
  .products{position:absolute;left:564px;top:630px;display:grid;grid-template-columns:116px 116px;column-gap:17px;row-gap:14px}
  .product-tile{width:116px;height:136px;background:var(--white);border-radius:12px;padding:14px;box-shadow:0 2px 6px rgba(0,0,0,.15)}
  .product-photo{width:100%;height:100%;border-radius:6px;background:radial-gradient(circle at 50% 50%,#cfd2d6 0%,#eceef0 70%,#ffffff 100%)}
  .product-photo.red{background:radial-gradient(circle at 50% 40%,#d93a3a 0%,#e9c9c9 55%,#ffffff 100%)}
  .product-photo.yellow{background:radial-gradient(circle at 50% 45%,#f2b716 0%,#f5e2a8 55%,#ffffff 100%)}
  .product-photo.dark{background:radial-gradient(circle at 50% 50%,#3a3d40 0%,#b9bcbf 55%,#ffffff 100%)}
  .makers{position:absolute;left:0;top:1098px;width:848px;height:102px;background:var(--band);display:flex;align-items:center}
  .maker{display:flex;align-items:center;justify-content:center;gap:6px;height:44px;color:#3b3b3b;font-weight:700;font-size:14px;line-height:1.05;text-align:center;border-right:1px solid #b9babd}
  .maker:last-child{border-right:none}
  .maker .dot{width:14px;height:14px;border-radius:50%;background:var(--red-deep);flex:none}
  .maker .sq{width:14px;height:14px;background:var(--red-deep);flex:none}
</style>
</head>
<body>
<main class="flyer">
  <div class="hero-photo" role="img" aria-label="Red fire hydrant on a grass verge with water gushing from its nozzle"></div>

  <svg class="shapes" width="848" height="1200" viewBox="0 0 848 1200" aria-hidden="true">
    <polygon points="368,0 848,0 848,94 410,94" fill="var(--white)"/>
    <polygon points="428,95 848,95 848,102 432,102" fill="var(--red)"/>
    <polygon points="460,430 848,430 848,620 502,718 457,657 368,657" fill="var(--red)"/>
    <polygon points="0,657 457,657 502,718 405,912 491,1098 0,1098" fill="var(--white)"/>
    <polygon points="548,579 559,579 405,912 424,912" fill="var(--red-deep)"/>
    <polygon points="559,579 848,579 848,1098 491,1098 405,912" fill="var(--panel-blue)"/>
  </svg>

  <header class="brand">
    <span class="brand-mark"></span>
    <span class="brand-name">Coastal Flowline Supply</span>
  </header>

  <h1 class="headline">
    <span class="main">FIRE HYDRANT</span>
    <span class="main">PARTS AND</span>
    <span class="sub">THE MANUFACTURERS</span>
  </h1>

  <section class="contact">
    <p class="cta">Call us Today!</p>
    <p class="phone">
      <svg width="38" height="38" viewBox="0 0 38 38" aria-hidden="true">
        <circle cx="19" cy="19" r="19" fill="var(--white)"/>
        <path d="M13 9c1-.6 2-.3 2.6.7l2 3.4c.5.9.3 1.9-.5 2.5l-1.3 1c.9 2 2.4 3.6 4.4 4.5l1-1.3c.6-.8 1.7-1 2.5-.5l3.4 2c1 .6 1.3 1.7.7 2.6l-1.2 1.9c-.7 1-2 1.5-3.2 1.2C16.6 25.6 12.4 21.4 11 14.6c-.3-1.2.2-2.5 1.2-3.2z" fill="var(--red)"/>
      </svg>(800) 555-0142</p>
    <p class="web">www.coastalflowline.com</p>
  </section>

  <ul class="parts-list">
    <li><svg width="18" height="18" viewBox="0 0 20 20" aria-hidden="true"><polygon points="10,1 12.6,7.4 19.5,7.6 14,11.8 16,18.5 10,14.6 4,18.5 6,11.8 0.5,7.6 7.4,7.4" fill="var(--red)"/></svg>Traffic Repair Kits</li>
    <li><svg width="18" height="18" viewBox="0 0 20 20" aria-hidden="true"><polygon points="10,1 12.6,7.4 19.5,7.6 14,11.8 16,18.5 10,14.6 4,18.5 6,11.8 0.5,7.6 7.4,7.4" fill="var(--red)"/></svg>Main Valve Repair Kits</li>
    <li><svg width="18" height="18" viewBox="0 0 20 20" aria-hidden="true"><polygon points="10,1 12.6,7.4 19.5,7.6 14,11.8 16,18.5 10,14.6 4,18.5 6,11.8 0.5,7.6 7.4,7.4" fill="var(--red)"/></svg>Extension Kits</li>
    <li><svg width="18" height="18" viewBox="0 0 20 20" aria-hidden="true"><polygon points="10,1 12.6,7.4 19.5,7.6 14,11.8 16,18.5 10,14.6 4,18.5 6,11.8 0.5,7.6 7.4,7.4" fill="var(--red)"/></svg>Replacement Caps &amp; Gaskets</li>
    <li><svg width="18" height="18" viewBox="0 0 20 20" aria-hidden="true"><polygon points="10,1 12.6,7.4 19.5,7.6 14,11.8 16,18.5 10,14.6 4,18.5 6,11.8 0.5,7.6 7.4,7.4" fill="var(--red)"/></svg>Replacement Nozzles</li>
    <li><svg width="18" height="18" viewBox="0 0 20 20" aria-hidden="true"><polygon points="10,1 12.6,7.4 19.5,7.6 14,11.8 16,18.5 10,14.6 4,18.5 6,11.8 0.5,7.6 7.4,7.4" fill="var(--red)"/></svg>Adjustable Hydrant Wrenches</li>
    <li><svg width="18" height="18" viewBox="0 0 20 20" aria-hidden="true"><polygon points="10,1 12.6,7.4 19.5,7.6 14,11.8 16,18.5 10,14.6 4,18.5 6,11.8 0.5,7.6 7.4,7.4" fill="var(--red)"/></svg>Hydrant Diffusers</li>
    <li><svg width="18" height="18" viewBox="0 0 20 20" aria-hidden="true"><polygon points="10,1 12.6,7.4 19.5,7.6 14,11.8 16,18.5 10,14.6 4,18.5 6,11.8 0.5,7.6 7.4,7.4" fill="var(--red)"/></svg>Hydrant Oil</li>
  </ul>

  <section class="products">
    <div class="product-tile"><div class="product-photo" role="img" aria-label="Adjustable hydrant wrench"></div></div>
    <div class="product-tile"><div class="product-photo dark" role="img" aria-label="Hydrant extension kit with flange, bolts and gaskets"></div></div>
    <div class="product-tile"><div class="product-photo red" role="img" aria-label="Red replacement hydrant cap with chain"></div></div>
    <div class="product-tile"><div class="product-photo yellow" role="img" aria-label="Yellow hydrant diffuser with pressure gauge"></div></div>
    <div class="product-tile"><div class="product-photo" role="img" aria-label="Bottle of hydrant oil"></div></div>
    <div class="product-tile"><div class="product-photo dark" role="img" aria-label="Traffic repair kit with breakaway flange and bolts"></div></div>
  </section>

  <footer class="makers">
    <div class="maker" style="width:166px"><span class="sq"></span>Ridgeline Valve<br>&amp; Hydrant</div>
    <div class="maker" style="width:142px"><span class="dot"></span>Kestrel Valve</div>
    <div class="maker" style="width:120px">Harbor Valve Co.</div>
    <div class="maker" style="width:142px"><span class="sq"></span>Northgate</div>
    <div class="maker" style="width:155px"><span class="dot"></span>Summit Flow<br>Control</div>
    <div class="maker" style="width:123px"><span class="dot"></span>Bayside Valve<br>Company</div>
  </footer>
</main>
</body>
</html>
```